Bright Harbor Real Estate Institute

This must be done in word press and I will need about 7 tabs The home page, Information page, Schedule and Cost page which will link to a Email me form, a online registration a about us and location/contact tab Each tab will then open several other pages. The home page will describe different courses that we offer since all the schools are about the same you can get a good ideal by going to qelvanto.org or pinnaclebayrealtyschool.com and looking at their site I would like mine to be similar as the courses are exactly the same but I would like the site to be more modern I also need it to be in word press so I can change it and update the dates as they change I have attached he logo below

Target Market(s)

people interested in getting into real estate and those who need continuing education

Coding

Coded - Design and coding required

Number of Pages Required

5+ page

Font styles to use
Sans Serif

Colors
3276b5

Requirements
Must have
• A page to schedule classes, a tab so the college I am partnering with can link the online courses to the back side, a page that describes the type of classes I offer

```html
<!DOCTYPE html>
<html lang="en">
<head>
<meta charset="utf-8">
<title>Bright Harbor Real Estate Institute – Schedule and Cost</title>
<link href="https://fonts.googleapis.com/css2?family=Comfortaa:wght@700&family=Crimson+Text:wght@400;600&family=Nunito:wght@400;600;700&display=swap" rel="stylesheet">
<style>
:root{
  --blue:#2b7de9;
  --ink:#222a33;
  --text:#5a5f66;
  --muted:#9aa0a6;
  --line:#dcdfe3;
  --footer-bg:#ececee;
  --white:#ffffff;
}
*{box-sizing:border-box;margin:0;padding:0}
html,body{width:1200px;height:4724px;overflow:hidden;background:var(--white)}
body{position:relative;font-family:"Nunito",sans-serif;color:var(--text)}
a{color:inherit;text-decoration:none}

.topbar{position:absolute;top:0;left:253px;width:947px;height:44px;background:var(--blue);display:flex;align-items:center;color:var(--white);font-family:"Crimson Text",serif;font-size:16px}
.topbar .social{display:flex;height:44px}
.topbar .social span{width:44px;height:44px;display:flex;align-items:center;justify-content:center;border-right:1px solid rgba(255,255,255,.35)}
.topbar .social span:first-child{border-left:1px solid rgba(255,255,255,.35)}
.topbar .social i{width:12px;height:12px;border-radius:50%;background:var(--white);display:block}
.topbar .service{margin-left:20px;display:flex;align-items:center;gap:10px}
.topbar .phone-badge{width:28px;height:28px;border-radius:50%;background:var(--white);display:flex;align-items:center;justify-content:center}
.topbar .phone-num{font-weight:600;font-size:19px;letter-spacing:.5px}
.topbar .addr{margin-left:22px;padding-left:18px;border-left:1px solid rgba(255,255,255,.35);height:44px;display:flex;align-items:center;gap:8px;font-size:14px}
.topbar .login{margin-left:auto;width:100px;height:44px;border-left:1px solid rgba(255,255,255,.35);display:flex;align-items:center;justify-content:center;font-weight:600;font-size:19px}

.header{position:absolute;top:44px;left:0;width:1200px;height:75px}
.brand{position:absolute;left:77px;top:19px;display:flex;align-items:center;gap:10px}
.brand-dot{width:24px;height:24px;border-radius:50%;background:var(--blue)}
.brand-name{font-weight:700;color:var(--blue);font-size:15px;line-height:18px;letter-spacing:.6px;text-transform:uppercase}
.nav{position:absolute;left:382px;top:28px;display:flex;gap:22px;font-size:14px;color:#4a4f55}
.nav .active{color:var(--blue)}

.hero{position:absolute;top:119px;left:0;width:1200px;height:360px;overflow:hidden}
.hero-photo{position:absolute;inset:0;background:linear-gradient(160deg,#6d6f72 0%,#9a9b9d 35%,#c9c8c6 60%,#8e8f91 100%)}
.hero-title{position:absolute;top:86px;left:0;width:1200px;text-align:center;font-family:"Comfortaa",sans-serif;font-weight:700;font-size:38px;color:var(--white);letter-spacing:-.3px}

.intro{position:absolute;top:545px;left:0;width:1200px;text-align:center}
.intro h2{font-family:"Crimson Text",serif;font-weight:600;font-size:38px;letter-spacing:.5px;color:var(--ink);text-transform:uppercase;line-height:54px}
.intro h2 span{color:var(--blue)}
.intro .rule{width:60px;height:3px;background:var(--blue);margin:6px auto 0}
.intro p{width:620px;margin:30px auto 0;font-size:14px;line-height:27px}
.payments{display:flex;justify-content:center;gap:22px;margin-top:22px}
.payments span{width:50px;height:30px;border-radius:3px;border:1px solid var(--line);background:#f4f6fa;display:flex;align-items:center;justify-content:center;font-size:10px;font-weight:700;color:var(--ink)}

.schedule-row{position:absolute;left:77px;width:1046px;display:grid;grid-template-columns:521px 525px}
.schedule-row.divided::before{content:"";position:absolute;left:0;right:0;top:-36px;height:1px;background:var(--line)}
.month h3{font-family:"Crimson Text",serif;font-weight:400;font-size:23px;line-height:50px;color:var(--ink)}
.course{margin-top:3px;margin-bottom:42px;font-size:13.5px;line-height:27.5px;letter-spacing:.6px}
.course + .course{margin-top:0}
.course .name{color:var(--blue);font-weight:600}
.register{display:inline-flex;align-items:center;gap:10px;margin-top:-15px;font-size:14px;line-height:27.5px;color:var(--blue);letter-spacing:.4px}

.footer{position:absolute;left:0;top:4230px;width:1200px;height:494px;background:var(--footer-bg)}
.newsletter{position:absolute;left:253px;top:57px;width:868px;height:123px;background:var(--blue);display:flex;align-items:center}
.newsletter h4{margin-left:44px;font-family:"Crimson Text",serif;font-weight:400;font-size:34px;line-height:46px;color:var(--white);width:320px}
.newsletter .field{margin-left:31px;width:279px;height:50px;border:1px solid rgba(255,255,255,.8);display:flex;align-items:center;padding-left:12px;font-size:14px;color:rgba(255,255,255,.9)}
.newsletter .btn{width:137px;height:50px;background:var(--white);color:var(--ink);display:flex;align-items:center;justify-content:center;font-family:"Crimson Text",serif;font-size:18px;letter-spacing:.6px}
.foot-brand{position:absolute;left:266px;top:206px;display:flex;align-items:center;gap:9px}
.foot-brand .brand-name{font-size:13px;line-height:16px}
.foot-brand .brand-dot{width:20px;height:20px}
.copyright{position:absolute;left:266px;top:282px;width:220px;text-align:center;font-size:12.5px;line-height:25px;color:var(--muted);letter-spacing:.4px}
.foot-col{position:absolute;top:204px}
.foot-col h5{font-family:"Crimson Text",serif;font-weight:400;font-size:19px;letter-spacing:1px;color:var(--ink);text-transform:uppercase;line-height:28px}
.foot-col .rule{width:40px;height:3px;background:var(--blue);margin-top:6px}
.links{left:556px}
.links ul{list-style:none;margin-top:18px}
.links li{font-size:13.5px;line-height:29px;color:var(--muted);letter-spacing:.4px}
.support{left:853px}
.support ul{list-style:none;margin-top:24px}
.support li{display:flex;gap:12px;font-size:13.5px;line-height:24px;color:var(--muted);letter-spacing:.5px;margin-bottom:11px}
.support svg{flex:none;margin-top:4px}
</style>
</head>
<body>

<div class="topbar">
  <div class="social" aria-label="Social links">
    <span><i></i></span><span><i></i></span><span><i></i></span>
  </div>
  <div class="service">
    Customer Services
    <span class="phone-badge"><svg width="16" height="16" viewBox="0 0 24 24"><path fill="#2b7de9" d="M6.6 10.8a15.1 15.1 0 0 0 6.6 6.6l2.2-2.2c.3-.3.7-.4 1-.2 1.1.4 2.3.6 3.6.6.6 0 1 .4 1 1V20c0 .6-.4 1-1 1A17 17 0 0 1 3 4c0-.6.4-1 1-1h3.5c.6 0 1 .4 1 1 0 1.3.2 2.5.6 3.6.1.3 0 .7-.2 1z"/></svg></span>
    <span class="phone-num">123 456 7890</span>
  </div>
  <div class="addr">
    <svg width="12" height="16" viewBox="0 0 12 16"><path fill="#fff" d="M6 0a6 6 0 0 0-6 6c0 4.5 6 10 6 10s6-5.5 6-10a6 6 0 0 0-6-6zm0 8.5A2.5 2.5 0 1 1 6 3.5a2.5 2.5 0 0 1 0 5z"/></svg>
    4180 Meridian Park Way, Alder Falls TN 37810
  </div>
  <a class="login" href="#">Login</a>
</div>

<header class="header">
  <div class="brand">
    <span class="brand-dot"></span>
    <span class="brand-name">Bright Harbor<br>Real Estate Institute</span>
  </div>
  <nav class="nav">
    <a class="active" href="#">★ Home</a>
    <a href="#">Courses</a>
    <a href="#">Information</a>
    <a href="#">Schedule And Cost</a>
    <a href="#">Registration</a>
    <a href="#">About Us</a>
    <a href="#">Location/Contact</a>
  </nav>
</header>

<section class="hero">
  <div class="hero-photo" role="img" aria-label="Photo of hands typing on a laptop keyboard"></div>
  <h1 class="hero-title">Online Pre-Licensing Registration</h1>
</section>

<section class="intro">
  <h2>Schedule and <span>Cost</span></h2>
  <div class="rule"></div>
  <p>We do not accept personal or business checks.The payment for course tuition will be collected in full on the first day of class.</p>
  <div class="payments" aria-label="Accepted payment methods">
    <span>Cardex</span><span>Versa</span><span>PayNest</span>
  </div>
</section>

<section class="schedule-row" style="top:780px">
  <div class="month">
    <h3>January 2020</h3>
    <div class="course"><span class="name">Pre-License</span> – Jan 6, 2020<br>Two-week Licensing course ($345.00)<br>60 credit hour<br>Day Class Mon-Fri 8:00 am- 1 pm<br>Night Classes: TBD</div>
    <div class="course"><span class="name">Course for New Affiliates</span>  – January 20, 2020<br>One-week Licensing course ($160.00)<br>Day Class: Mon-Fri 8:00 am – 1 pm<br>Night Class: TBD</div>
    <a class="register" href="#">Register <svg width="26" height="10" viewBox="0 0 26 10"><path d="M0 5h24M20 1l4 4-4 4" fill="none" stroke="#2b7de9" stroke-width="1.4"/></svg></a>
  </div>
  <div class="month">
    <h3>February 2020</h3>
    <div class="course"><span class="name">Pre-License</span> – Feb 3, 2020<br>Two-week Licensing course ($345.00)<br>60 credit hour<br>Day Class Mon-Fri 8:00 am- 1 pm<br>Night Classes: TBD</div>
    <div class="course"><span class="name">Course for New Affiliates</span>  – January 17, 2020<br>One-week Licensing course ($160.00)<br>Day Class: Mon-Fri 8:00 am – 1 pm<br>Night Class: TBD</div>
    <a class="register" href="#">Register <svg width="26" height="10" viewBox="0 0 26 10"><path d="M0 5h24M20 1l4 4-4 4" fill="none" stroke="#2b7de9" stroke-width="1.4"/></svg></a>
  </div>
</section>

<section class="schedule-row divided" style="top:1249px">
  <div class="month">
    <h3>March 2020</h3>
    <div class="course"><span class="name">Pre-License</span> – March 2, 2020<br>Two-week Licensing course ($345.00)<br>60 Credit Hours<br>Day Class: Mon – Fri 8:00 am – 1 pm<br>Night Class: TBD</div>
    <div class="course"><span class="name">Course for New Affiliates</span>  – March 16, 2020<br>One-week Licensing course ($165.00)<br>30 Credit Hours<br>Day Class: Mon – Fri 8:00 am – 1 pm<br>Night Class: TBD</div>
    <div class="course"><span class="name">Broker Management</span>   – TBD<br>One-week Licensing course ($195.00)<br>30 Credit Hours<br>Day Class: Mon – Fri 8:00 am – 2 pm</div>
    <a class="register" href="#">Register <svg width="26" height="10" viewBox="0 0 26 10"><path d="M0 5h24M20 1l4 4-4 4" fill="none" stroke="#2b7de9" stroke-width="1.4"/></svg></a>
  </div>
  <div class="month">
    <h3>April 2020</h3>
    <div class="course"><span class="name">Pre-License</span> – April 6, 2020 (9-Day Class)<br>Two-week Licensing course ($345.00)<br>60 Credit Hours<br>Day Class: Mon – Fri 8:00 am – 1 pm<br>Night Class: TBD</div>
    <div class="course"><span class="name">Course for New Affiliates</span>  – April 20, 2020<br>One-week Licensing course ($165.00)<br>30 Credit Hours<br>Day Class: Mon – Fri 8:00 am – 1 pm<br>Night Class: TBD</div>
    <a class="register" href="#">Register <svg width="26" height="10" viewBox="0 0 26 10"><path d="M0 5h24M20 1l4 4-4 4" fill="none" stroke="#2b7de9" stroke-width="1.4"/></svg></a>
  </div>
</section>

<section class="schedule-row divided" style="top:1885px">
  <div class="month">
    <h3>May 2020</h3>
    <div class="course"><span class="name">Pre-License</span> – May 11, 2020<br>Two-week Licensing course ($345.00)<br>60 Credit Hours<br>Day Class: Mon – Fri 8:00 am – 1 pm<br>Night Class: TBD</div>
    <div class="course"><span class="name">Course for New Affiliates</span>  – May 26, 2020<br>One-week Licensing course ($165.00)<br>30 Credit Hours<br>Day Class: Mon – Fri 8:00 am – 1 pm<br>Night Class: TBD</div>
    <a class="register" href="#">Register <svg width="26" height="10" viewBox="0 0 26 10"><path d="M0 5h24M20 1l4 4-4 4" fill="none" stroke="#2b7de9" stroke-width="1.4"/></svg></a>
  </div>
  <div class="month">
    <h3>June 2020</h3>
    <div class="course"><span class="name">Pre-License</span> – June 1, 2020<br>Two-week Licensing course ($345.00)<br>60 Credit Hours<br>Day Class: Mon – Fri 8:00 am – 1 pm<br>Night Class: TBD</div>
    <div class="course"><span class="name">Course for New Affiliates</span>  – June 15, 2020<br>One-week Licensing course ($165.00)<br>30 Credit Hours<br>Day Class: Mon – Fri 8:00 am – 1 pm<br>Night Class: TBD</div>
    <div class="course"><span class="name">Broker Management</span>  – TBD<br>One-week Licensing course ($195.00)<br>30 Credit Hours<br>Day Class: Mon – Fri 8:00 am – 2 pm</div>
    <a class="register" href="#">Register <svg width="26" height="10" viewBox="0 0 26 10"><path d="M0 5h24M20 1l4 4-4 4" fill="none" stroke="#2b7de9" stroke-width="1.4"/></svg></a>
  </div>
</section>

<section class="schedule-row divided" style="top:2526px">
  <div class="month">
    <h3>July 2020</h3>
    <div class="course"><span class="name">Pre-License</span> – July 6, 2020<br>Two-week Licensing course ($345.00)<br>60 Credit Hours<br>Day Class: Mon – Fri 8:00 am – 1 pm<br>Night Class: TBD</div>
    <div class="course"><span class="name">Course for New Affiliates</span>  – July 20, 2020<br>One-week Licensing course ($165.00)<br>30 Credit Hours<br>Day Class: Mon – Fri 8:00 am – 1 pm<br>Night Class: TBD</div>
    <a class="register" href="#">Register <svg width="26" height="10" viewBox="0 0 26 10"><path d="M0 5h24M20 1l4 4-4 4" fill="none" stroke="#2b7de9" stroke-width="1.4"/></svg></a>
  </div>
  <div class="month">
    <h3>August 2020</h3>
    <div class="course"><span class="name">Pre-License</span> – August 3, 2020<br>Two-week Licensing course ($345.00)<br>60 Credit Hours<br>Day Class: Mon – Fri 8:00 am – 1 pm<br>Night Class: TBD</div>
    <div class="course"><span class="name">Course for New Affiliates</span>  – August 17, 2020<br>One-week Licensing course ($165.00)<br>30 Credit Hours<br>Day Class: Mon – Fri 8:00 am – 1 pm<br>Night Class: TBD</div>
    <div class="course"><span class="name">Broker Management</span>  – TBD<br>One-week Licensing course ($195.00)<br>30 Credit Hours</div>
    <a class="register" href="#">Register <svg width="26" height="10" viewBox="0 0 26 10"><path d="M0 5h24M20 1l4 4-4 4" fill="none" stroke="#2b7de9" stroke-width="1.4"/></svg></a>
  </div>
</section>

<section class="schedule-row divided" style="top:3140px">
  <div class="month">
    <h3>September 2020</h3>
    <div class="course"><span class="name">Pre-License</span> – September 8, 2020 (9-Day Class)<br>Two-week Licensing course ($345.00)<br>60 Credit Hours<br>Day Class: Mon – Fri 8:00 am – 1 pm<br>Night Class: TBD</div>
    <div class="course"><span class="name">Course for New Affiliates</span>  – September 21, 2020<br>One-week Licensing course ($165.00)<br>30 Credit Hours<br>Day Class: Mon – Fri 8:00 am – 1 pm<br>Night Class: TBD</div>
    <a class="register" href="#">Register <svg width="26" height="10" viewBox="0 0 26 10"><path d="M0 5h24M20 1l4 4-4 4" fill="none" stroke="#2b7de9" stroke-width="1.4"/></svg></a>
  </div>
  <div class="month">
    <h3>October 2020</h3>
    <div class="course"><span class="name">Pre-License</span> – October 5, 2020<br>Two-week Licensing course ($345.00)<br>60 Credit Hours<br>Day Class: Mon – Fri 8:00 am – 1 pm<br>Night Class: TBD</div>
    <div class="course"><span class="name">Course for New Affiliates</span>  – October 19, 2020<br>One-week Licensing course ($165.00)<br>30 Credit Hours<br>Day Class: Mon – Fri 8:00 am – 1 pm<br>Night Class: TBD</div>
    <a class="register" href="#">Register <svg width="26" height="10" viewBox="0 0 26 10"><path d="M0 5h24M20 1l4 4-4 4" fill="none" stroke="#2b7de9" stroke-width="1.4"/></svg></a>
  </div>
</section>

<section class="schedule-row divided" style="top:3641px">
  <div class="month">
    <h3>November 2020</h3>
    <div class="course"><span class="name">Pre-License</span> – November 2, 2020<br>Two-week Licensing course ($345.00)<br>60 Credit Hours<br>Day Class: Mon – Fri 8:00 am – 1 pm<br>Night Class: TBD</div>
    <div class="course"><span class="name">Course for New Affiliates</span>  – November 16, 2020<br>One-week Licensing course ($165.00)<br>30 Credit Hours<br>Day Class: Mon – Fri 8:00 am – 1 pm<br>Night Class: TBD</div>
    <a class="register" href="#">Register <svg width="26" height="10" viewBox="0 0 26 10"><path d="M0 5h24M20 1l4 4-4 4" fill="none" stroke="#2b7de9" stroke-width="1.4"/></svg></a>
  </div>
  <div class="month">
    <h3>December 2020</h3>
    <div class="course"><span class="name">Pre-License</span> – December class begins 11/30/20<br>Two-week Licensing course ($345.00)<br>60 Credit Hours<br>Day Class: Mon – Fri 8:00 am – 1 pm<br>Night Class: TBD</div>
    <div class="course"><span class="name">Course for New Affiliates</span>  – December 14, 2020<br>One-week Licensing course ($165.00)<br>30 Credit Hours<br>Day Class: Mon – Fri 8:00 am – 1 pm<br>Night Class: TBD<br>is schedule</div>
    <a class="register" href="#">Register <svg width="26" height="10" viewBox="0 0 26 10"><path d="M0 5h24M20 1l4 4-4 4" fill="none" stroke="#2b7de9" stroke-width="1.4"/></svg></a>
  </div>
</section>

<footer class="footer">
  <div class="newsletter">
    <h4>Join Our Newsletter &amp; Update</h4>
    <div class="field">Enter email here...</div>
    <div class="btn">SUBSCRIBE</div>
  </div>
  <div class="foot-brand">
    <span class="brand-dot"></span>
    <span class="brand-name">Bright Harbor<br>Real Estate Institute</span>
  </div>
  <p class="copyright">© BRIGHT HARBOR REAL ESTATE INSTITUTE -2019 All Rights Reserved.</p>
  <div class="foot-col links">
    <h5>Quick Links</h5>
    <div class="rule"></div>
    <ul>
      <li>Home</li><li>Courses</li><li>Information</li><li>Schedule And Cost</li><li>Registration</li><li>About Us</li><li>Location/Contact</li>
    </ul>
  </div>
  <div class="foot-col support">
    <h5>Support</h5>
    <div class="rule"></div>
    <ul>
      <li><svg width="16" height="16" viewBox="0 0 24 24"><path fill="#2b7de9" d="M6.6 10.8a15.1 15.1 0 0 0 6.6 6.6l2.2-2.2c.3-.3.7-.4 1-.2 1.1.4 2.3.6 3.6.6.6 0 1 .4 1 1V20c0 .6-.4 1-1 1A17 17 0 0 1 3 4c0-.6.4-1 1-1h3.5c.6 0 1 .4 1 1 0 1.3.2 2.5.6 3.6.1.3 0 .7-.2 1z"/></svg>123 456 7890</li>
      <li><svg width="18" height="14" viewBox="0 0 18 14"><rect width="18" height="14" rx="2" fill="#2b7de9"/><path d="M1 2l8 6 8-6" fill="none" stroke="#fff" stroke-width="1.5"/></svg>info@brightharbor.com</li>
      <li><svg width="14" height="20" viewBox="0 0 12 16"><path fill="#2b7de9" d="M6 0a6 6 0 0 0-6 6c0 4.5 6 10 6 10s6-5.5 6-10a6 6 0 0 0-6-6zm0 8.5A2.5 2.5 0 1 1 6 3.5a2.5 2.5 0 0 1 0 5z"/></svg><span>101 - Address, City<br>Pincode Zip.</span></li>
    </ul>
  </div>
</footer>

</body>
</html>
```